Heading: Tarraway (small font: under Tarraway.. LIVE IN NOOSA)

We need a flyer for an upcoming Live show. (Double sided DL)
It is a magic & comedy show . We would like it to feel like its a high end classy show as it will be at a 5 star hotel. We like the look of all the Théâtre des Ombres posters (maybe google to have a look - I have attached some examples of what we like.
INFO FOR FLYER DOUBLE SIDED DL FLYER
Promo Photo- FOR FRONT OF FLYER : https://www.filedrop-example.com/s/kq7trzp2mwx/Lorne%20Baxter%20Studio%20%28358%20of%20530%29.jpg?dl=0
A world-class experience combining comedy, magic and illusion.
Tarraway has Performed live to over 1 million people.
*****
“HIGHLY ENTERTAINING (add 5 star graphics)
SENSATIONAL SHOW”
Marla Quintrell
*****
"TARRAWAY’S SHOW WAS BETTER THAN HARGROVE IN VEGAS. LOVED IT!”
Jocelyn & Warren Pitcairn
*****
“BEST MAGIC SHOW I’VE SEEN…
HAD US IN STITCHES LAUGHING THE WHOLE TIME”
Pepita Lou
SESSION ONE
FAMILY SHOW 5:30PM $38 PP
SESSION TWO
LATE SESSION 8PM $49.00 PP
NOOSA DATES
Thursday 24th Sept
Saturday 26th Sept
Thursday 1st October
Saturday 3rd October
BOOK ONLINE NOW - www.tarraway.com.au
BRAMBLEWOOD RESORT NOOSA LOGO (NEAR THE BOTTOM)
BACK OF FLYER
Add dinner to your award-winning show experience.
Supper at Ridge by Owen Trevallick (ADD LOGO)
Two courses including a glass of wine $39.00
Two sittings, 6.30pm and 7pm.
Tables limited, so please book early to secure your table.
Booking details via Tarraway.com.au
Ridge Bar
Open from 12pm daily.
BRAMBLEWOOD Resort LOGO
Only a 5 minute stroll from Corrigan Street, Noosa Heads
Vehicle Entry/Exit
Vehicle entry/exit as follows:
Tallowood Drive (7pm-7am, Little Corrigan Street),
Kestrelbank Drive (7am-7pm, Orla Way).
(please add map)
On-Site Parking
Limited parking is available on-site. Once parking is full, guests will be directed to park on Kestrelbank Drive, with the resort buggy service available to transport guests up/down the driveway.
Covid Safety, Contact Tracing & distancing regulations are in place.
More Info: www.tarraway.com.au

```html
<!DOCTYPE html>
<html lang="en">
<head>
<meta charset="utf-8">
<title>Tarraway – Live in Noosa – DL Flyer</title>
<link href="https://fonts.googleapis.com/css2?family=Arimo:wght@400;700&family=Oswald:wght@400;500&family=Rye&family=Cinzel:wght@400;700&display=swap" rel="stylesheet">
<style>
  :root {
    --page: #f4f4f4;
    --purple-deep: #2a0b3d;
    --purple: #4a1150;
    --magenta: #b2204a;
    --red: #e2402c;
    --orange: #f47a22;
    --amber: #ffb347;
    --gold: #f3c24a;
    --white: #ffffff;
    --text: #ffffff;
    --panel: rgba(40, 8, 50, 0.28);
  }
  * { box-sizing: border-box; margin: 0; padding: 0; }
  html, body {
    width: 1200px; height: 1200px; overflow: hidden;
    background: var(--page);
  }
  .flyer {
    position: absolute; top: 222px;
    width: 535px; height: 756px; overflow: hidden;
    color: var(--text);
    font-family: "Arimo", Arial, sans-serif;
    background:
      radial-gradient(ellipse 70% 45% at 50% 45%, rgba(255,170,60,.85), rgba(255,120,40,0) 70%),
      linear-gradient(180deg, var(--purple) 0%, var(--magenta) 14%, var(--red) 30%, var(--orange) 48%, var(--red) 66%, var(--magenta) 80%, var(--purple-deep) 100%);
  }
  .flyer--front { left: 48px; }
  .flyer--back { left: 617px; }
  .flyer__lines { position: absolute; inset: 0; width: 100%; height: 100%; }
  .centered { position: absolute; left: 0; right: 0; text-align: center; }

  /* front */
  .intro { top: 11px; font-size: 9.6px; line-height: 15px; letter-spacing: .3px; }
  .halo {
    position: absolute; left: 130px; top: 75px; width: 276px; height: 276px;
    border-radius: 50%; border: 2px solid rgba(255,200,90,.8);
    box-shadow: 0 0 18px rgba(255,190,80,.7), inset 0 0 18px rgba(255,190,80,.5);
  }
  .promo-photo {
    position: absolute; left: 163px; top: 56px; width: 196px; height: 350px;
    border-radius: 90px 90px 6px 6px;
    background: linear-gradient(180deg, #e8b89a 0%, #d19b80 16%, #1a1418 24%, #0e0b0e 100%);
  }
  .headline {
    top: 400px; font-family: "Rye", Georgia, serif; font-size: 76px; line-height: 90px;
    color: #eeeeee; letter-spacing: -1px; transform: scaleX(.86);
    text-shadow: 0 3px 0 #7a7a7a, 0 6px 10px rgba(0,0,0,.6);
  }
  .subhead {
    top: 490px; font-family: "Rye", Georgia, serif; font-size: 25px; letter-spacing: 9px;
    color: #d8d8d8; text-shadow: 0 2px 0 #555;
  }
  .review {
    position: absolute; top: 532px; width: 160px; text-align: center;
    font-family: "Oswald", sans-serif; font-size: 11.5px; line-height: 11.5px; letter-spacing: .5px;
    transform: translateX(-50%);
  }
  .review__stars { font-size: 19px; letter-spacing: 1px; line-height: 22px; margin-bottom: 4px; }
  .review__author { display: block; font-size: 8px; font-style: italic; }
  .sessions {
    position: absolute; left: 89px; top: 602px; width: 357px; height: 47px;
    border: 1.5px solid var(--white); display: flex;
  }
  .session {
    flex: 1; text-align: center; font-family: "Oswald", sans-serif; font-size: 14px; line-height: 19px;
    padding-top: 4px; transform: scaleX(.9);
  }
  .session + .session { border-left: 1.5px solid var(--white); }
  .dates-title { top: 654px; font-family: "Oswald", sans-serif; font-size: 12px; }
  .dates { top: 668px; font-family: "Oswald", sans-serif; font-size: 11.5px; letter-spacing: .2px; }
  .book { top: 685px; font-family: "Oswald", sans-serif; font-size: 14px; letter-spacing: 2.5px; }
  .resort-name {
    position: absolute; left: 0; right: 0; top: 712px; text-align: center;
    font-family: "Cinzel", serif; font-size: 11px; letter-spacing: 2px; color: var(--white);
  }
  .resort-name::before {
    content: ""; display: inline-block; width: 7px; height: 7px; background: var(--white);
    margin-right: 6px; vertical-align: 1px;
  }

  /* back */
  .back-panel { position: absolute; left: 29px; top: 28px; width: 478px; height: 700px; background: var(--panel); }
  .back-copy { font-size: 9.6px; line-height: 14.6px; letter-spacing: .3px; }
  .back-copy strong { font-weight: 700; letter-spacing: .8px; }
  .back-heading { top: 64px; font-size: 11.5px; font-weight: 700; letter-spacing: 1px; text-decoration: underline; }
  .venue-name {
    position: absolute; left: 0; right: 0; text-align: center; color: var(--white);
    font-family: "Cinzel", serif;
  }
  .venue-name--dinner { top: 117px; font-size: 22px; letter-spacing: 4px; line-height: 26px; }
  .venue-name--dinner small { display: block; font-size: 8px; letter-spacing: 1.5px; line-height: 10px; }
  .venue-name--resort { top: 302px; font-size: 13px; letter-spacing: 2px; }
  .venue-name--resort::before {
    content: ""; display: inline-block; width: 8px; height: 8px; background: var(--white);
    margin-right: 6px; vertical-align: 1px;
  }
  .location-map {
    position: absolute; left: 185px; top: 428px; width: 161px; height: 129px;
    background: linear-gradient(90deg, #f1f1ef 0%, #ececea 70%, #cfe8d8 78%, #bfe1cc 100%);
  }
</style>
</head>
<body>

<section class="flyer flyer--front" aria-label="Flyer front">
  <svg class="flyer__lines" viewBox="0 0 535 756" aria-hidden="true" fill="none" stroke="#ffb24a" stroke-width="1.6" opacity=".75">
    <path d="M268 60 L500 290 L268 520 L36 290 Z"/>
    <path d="M268 100 L460 290 L268 480 L76 290 Z" opacity=".6"/>
    <path d="M268 520 L470 720 M268 520 L66 720" opacity=".5"/>
    <line x1="10" y1="60" x2="200" y2="420"/>
    <line x1="525" y1="60" x2="335" y2="420"/>
    <line x1="470" y1="0" x2="300" y2="200"/>
  </svg>
  <p class="centered intro">A WORLD-CLASS EXPERIENCE COMBINING COMEDY, MAGIC AND ILLUSION.<br>TARRAWAY HAS PERFORMED LIVE TO OVER 1 MILLION PEOPLE.</p>
  <div class="halo" aria-hidden="true"></div>
  <div class="promo-photo" role="img" aria-label="Promo photo of the performer in a black velvet jacket"></div>
  <h1 class="centered headline">TARRAWAY</h1>
  <p class="centered subhead">LIVE IN NOOSA</p>

  <div class="review" style="left:115px">
    <div class="review__stars">★★★★★</div>
    “HIGHLY ENTERTAINING<br>SENSATIONAL SHOW”
    <span class="review__author">-MARLA QUINTRELL</span>
  </div>
  <div class="review" style="left:246px">
    <div class="review__stars">★★★★★</div>
    "TARRAWAY’S SHOW WAS<br>BETTER THAN HARGROVE<br>IN VEGAS. LOVED IT!”
    <span class="review__author">-JOCELYN &amp; WARREN PITCAIRN</span>
  </div>
  <div class="review" style="left:400px">
    <div class="review__stars">★★★★★</div>
    “BEST MAGIC SHOW<br>I’VE SEEN… HAD US IN STITCHES<br>LAUGHING THE WHOLE TIME”
    <span class="review__author">-PEPITA LOU</span>
  </div>

  <div class="sessions">
    <div class="session">SESSION ONE<br>FAMILY SHOW 5:30PM $38 PP</div>
    <div class="session">SESSION TWO<br>LATE SESSION 8PM $49.00 PP</div>
  </div>
  <p class="centered dates-title">NOOSA DATES:</p>
  <p class="centered dates">THURSDAY 24TH SEPT | SATURDAY 26TH SEPT | THURSDAY 1ST OCTOBER | SATURDAY 3RD OCTOBER</p>
  <p class="centered book">BOOK ONLINE NOW - WWW.TARRAWAY.COM.AU</p>
  <p class="resort-name">BRAMBLEWOOD</p>
</section>

<section class="flyer flyer--back back-copy" aria-label="Flyer back">
  <svg class="flyer__lines" viewBox="0 0 535 756" aria-hidden="true" fill="none" stroke="#ffb24a" stroke-width="1.6" opacity=".7">
    <path d="M268 40 L515 290 L268 540 L21 290 Z"/>
    <path d="M268 240 L515 480 L268 720 L21 480 Z" opacity=".6"/>
    <line x1="20" y1="40" x2="260" y2="420"/>
    <line x1="515" y1="40" x2="275" y2="420"/>
    <line x1="30" y1="740" x2="190" y2="520"/>
    <line x1="505" y1="740" x2="345" y2="520"/>
  </svg>
  <div class="back-panel" aria-hidden="true"></div>
  <p class="centered back-heading">ADD DINNER TO YOUR AWARD-WINNING SHOW EXPERIENCE</p>
  <p class="centered" style="top:94px"><strong>DINNER:</strong></p>
  <p class="venue-name venue-name--dinner">RIDGE<small>BY OWEN TREVALLICK</small></p>
  <p class="centered" style="top:167px">TWO COURSES INCLUDING A GLASS OF WINE $39.00<br>TWO SITTINGS - 6:30PM AND 7:0PM.<br>TABLES LIMITED, SO PLEASE BOOK EARLY TO SECURE YOUR TABLE.<br><strong>BOOKING DETAILS VIA TARRAWAY.COM.AU</strong></p>
  <p class="centered" style="top:255px"><strong>RIDGE BAR</strong><br>OPEN FROM 12:00PM DAILY.</p>
  <p class="venue-name venue-name--resort">BRAMBLEWOOD</p>
  <p class="centered" style="top:341px">ONLY A 5 MINUTE STROLL FROM CORRIGAN STREET, NOOSA HEADS<br>VEHICLE ENTRY/EXIT<br>VEHICLE ENTRY/EXIT AS FOLLOWS:<br>TALLOWOOD DRIVE (7:00PM-7:00AM, LITTLE CORRIGAN STREET),<br>KESTRELBANK DRIVE (7:00AM-7:00PM, ORLA WAY).</p>
  <div class="location-map" role="img" aria-label="Street map showing the resort location near Noosa Heads"></div>
  <p class="centered" style="top:561px">ON-SITE PARKING<br>LIMITED PARKING IS AVAILABLE ON-SITE. ONCE PARKING IS FULL,<br>GUESTS WILL BE DIRECTED TO PARK ON KESTRELBANK DRIVE,<br>WITH THE RESORT BUGGY SERVICE AVAILABLE<br>TO TRANSPORT GUESTS UP/DOWN THE DRIVEWAY.</p>
  <p class="centered" style="top:649px"><strong>COVID SAFETY, CONTACT TRACING &amp; DISTANCING REGULATIONS ARE IN PLACE.</strong><br>MORE INFO: <strong>WWW.TARRAWAY.COM.AU</strong></p>
</section>

</body>
</html>
```